GLP letterhead

We need a letterhead design for our new company based in Los Angeles called "Gold Lantern Pictures". We develop film and television projects. We work with investors, financiers, film production companies, film distribution and sales companies as well as studios. We would like to incorporate our logo (see attached) but make the letterhead simple and elegant. We need to include: logo, company address, phone number and company website.
Updates

Hello designers, Thanks for your submissions. For our letterhead, we are looking for something more simple and elegant. No heavy bars or lines. Make it feel light and clean. Not a lot of ink on the page. Use the logo and contact info but think "clean", "streamlined" and mostly white paper. Looking forward to seeing more... thanks! Gold Lantern Pictures team

Target Market(s)

Studio executives, talent agents and agencies, financiers, investors.

Industry/Entity Type

It Company

Requirements
Must have
• Gold Lantern Pictures logo (see attached). Logo may be cropped and altered appropriately for elegant letterhead design.
• Please include:
• COMPANY ADDRESS:
• Ridgeway Studio Park
• 2850 Halverson Street
• Tower Annex, Suite 6
• Corliss Bay, OR 97541
• COMPANY WEBSITE:
• www.goldlanternpicturesco.example
• COMPANY PHONE NUMBER:
• 555-555-0148

```html
<!DOCTYPE html>
<html lang="en">
<head>
<meta charset="utf-8">
<title>Gold Lantern Pictures Letterhead</title>
<link href="https://fonts.googleapis.com/css2?family=Arimo:wght@400&family=Tinos:wght@400&family=Great+Vibes&display=swap" rel="stylesheet">
<style>
  :root {
    --backdrop: #8f9ba1;
    --paper: #f7f7f7;
    --ink: #2a2a2a;
    --logo-block: #151515;
    --logo-accent: #3fb3d6;
    --footer-ink: #333333;
  }
  * { margin: 0; padding: 0; box-sizing: border-box; }
  html, body {
    width: 1200px;
    height: 794px;
    overflow: hidden;
    background: var(--backdrop);
  }
  .letterhead {
    position: absolute;
    left: 331px;
    top: 17px;
    width: 538px;
    height: 760px;
    background: var(--paper);
    box-shadow: 0 4px 18px rgba(0, 0, 0, 0.25);
  }
  .brand-block {
    position: absolute;
    left: 210px;
    top: 0;
    width: 134px;
    height: 92px;
    background: var(--logo-block);
    display: flex;
    align-items: center;
    justify-content: center;
    gap: 6px;
    padding: 0 8px;
  }
  .brand-mark {
    width: 9px;
    height: 9px;
    border-radius: 50%;
    background: var(--logo-accent);
    flex: none;
  }
  .brand-name {
    font-family: "Arimo", Arial, sans-serif;
    font-size: 10px;
    letter-spacing: 0.08em;
    text-transform: uppercase;
    color: var(--logo-accent);
    line-height: 1.3;
  }
  .letter-body {
    position: absolute;
    left: 64px;
    top: 150px;
    width: 410px;
    font-family: "Tinos", "Times New Roman", serif;
    font-size: 10.5px;
    line-height: 1.62;
    color: var(--ink);
  }
  .letter-body p { margin-bottom: 15px; }
  .closing {
    margin-top: 28px;
    font-family: "Tinos", "Times New Roman", serif;
    font-size: 12px;
  }
  .signature {
    font-family: "Great Vibes", cursive;
    font-size: 19px;
    margin-top: 2px;
    color: #111;
  }
  .contact-footer {
    position: absolute;
    right: 40px;
    bottom: 34px;
    text-align: right;
    font-family: "Arimo", Arial, sans-serif;
    font-size: 9px;
    line-height: 1.6;
    color: var(--footer-ink);
    white-space: nowrap;
  }
  .contact-footer .phone { margin-left: 14px; }
</style>
</head>
<body>
  <main class="letterhead">
    <header class="brand-block">
      <span class="brand-mark"></span>
      <span class="brand-name">Gold Lantern Pictures</span>
    </header>

    <section class="letter-body">
      <p>Lorem ipsum dolor sit amet, consectetur adipiscing elit. Donec elementum maximus mi vel placerat. Sed aliquet, erat nec aliquet euismod, nisi leo rhoncus purus, sed pretium justo risus et velit. Ut varius vitae risus a viverra. Vestibulum eu viverra magna. Sed id euismod mi. Curabitur dignissim volutpat neque et feugiat. Vestibulum mollis felis eu laoreet varius. Sed et nunc sodales, euismod odio vitae, consectetur neque. Ut tempus libero mattis posuere porttitor. In vel felis vulputate, porta nisl id, faucibus lectus.</p>
      <p>Aenean in turpis sagittis, finibus est sit amet, tempus enim. Nam leo dui, bibendum nec mattis vitae, euismod sit risus. Nunc facilisis ex vitae dictum venenatis. Sed sapien elit, tempor non justo non, venenatis lacinia velit. Praesent feugiat purus eget neque porttitor, quis commodo dolor luctus. Nunc aliquet auctor ante, suscipit commodo risus ultricies maximus. Aliquam at risus nec nulla hendrerit consectetur a id lectus. Mauris imperdiet ante quis lobortis placerat. Sed rutrum nec libero eu finibus. Cras varius tincidunt tincidunt. Vivamus elementum vitae enim vehicula iaculis. Nullam hendrerit arcu in pharetra blandit. Aliquam quis orci iaculis, rutrum mauris non, pellentesque sapien. Pellentesque quis erat accumsan, faucibus metus nec, laoreet ante.</p>
      <div class="closing">Sincerly,</div>
      <div class="signature">Name Here</div>
    </section>

    <footer class="contact-footer">
      <div><span class="website">www.goldlanternpicturesco.example</span><span class="phone">555-555-0148</span></div>
      <div class="address">Ridgeway Studio Park 2850 Halverson Street Tower Annex, Suite 6 Corliss Bay, OR 97541</div>
    </footer>
  </main>
</body>
</html>
```